Self Help / Psychology Ebook Cover Design

Looking for a design based on the concept of the I AM (You) placed at the centre of a radar screen. The design should communicate the concept of using our built in human radar coupled with intuition to navigate to a new life that we are actively creating. <br/>The image attached is to give a visual brief / idea / concept. BUT you are NOT restricted to this. <br/>The RADAR concept is featured in the book and a key element to what they book sets out to achieve.<br/>The TITLE of the book will need to be on the cover.<br/>SEVEN QUIET DOORS TOWARD A BRIGHTER MORNING.<br/><br/>Author Name to be at the foot of the book similar to the design on one of my earlier books. You can view that book cover at.<br/>https://dorianwaite.net/<br/>
Self help / psychology / success

```html
<!DOCTYPE html>
<html lang="en">
<head>
<meta charset="utf-8">
<title>Seven Quiet Doors Toward a Brighter Morning — Cover</title>
<link rel="stylesheet" href="https://fonts.googleapis.com/css2?family=Bebas+Neue&family=Oswald:wght@300&family=Arimo:wght@700&display=swap">
<style>
  :root {
    --page: #ffffff;
    --cover: #000000;
    --ink: #ffffff;
    --accent: #5ce61a;
    --accent-glow: #8dff55;
    --accent-deep: #2f9a0e;
    --author-ink: #111111;
  }
  * { box-sizing: border-box; margin: 0; padding: 0; }
  html, body {
    width: 1200px;
    height: 1200px;
    overflow: hidden;
    background: var(--page);
  }
  .stage {
    width: 1200px;
    height: 1200px;
    display: flex;
    align-items: center;
    justify-content: center;
  }
  .cover {
    position: relative;
    width: 640px;
    height: 1000px;
    background: var(--cover);
    display: flex;
    flex-direction: column;
    overflow: hidden;
  }
  .title {
    flex: 1;
    display: flex;
    flex-direction: column;
    align-items: center;
    justify-content: center;
    padding: 30px 40px 20px;
    text-align: center;
    color: var(--ink);
    font-family: "Bebas Neue", "Oswald", sans-serif;
    font-weight: 400;
    line-height: 0.86;
  }
  .title__lead {
    font-family: "Oswald", sans-serif;
    font-weight: 300;
    color: var(--accent);
    font-size: 80px;
    line-height: 1;
    letter-spacing: 1px;
    margin-bottom: 16px;
  }
  .title__line--big { font-size: 190px; }
  .title__line--hero {
    font-size: 172px;
    display: flex;
    align-items: center;
    justify-content: center;
    gap: 6px;
    margin: 14px 0 18px;
  }
  .title__line--mid { font-size: 120px; margin-bottom: 10px; }
  .title__line--end { font-size: 190px; }
  .radar-head {
    flex: none;
    width: 124px;
    height: 146px;
    border-radius: 50%;
    background: radial-gradient(circle at 50% 45%, var(--accent-glow) 0%, var(--accent) 45%, var(--accent-deep) 100%);
  }
  .author-band {
    height: 112px;
    background: var(--accent);
    display: flex;
    align-items: center;
    justify-content: center;
  }
  .author-band__name {
    font-family: "Arimo", Arial, sans-serif;
    font-weight: 700;
    font-size: 44px;
    letter-spacing: 1px;
    color: var(--author-ink);
  }
</style>
</head>
<body>
  <main class="stage">
    <article class="cover">
      <h1 class="title">
        <span class="title__lead">SEVEN QUIET</span>
        <span class="title__line--big">DOORS</span>
        <span class="title__line--hero">
          <span>T</span>
          <span class="radar-head" role="img" aria-label="Green head silhouette in profile with a glowing radar screen inside, standing in for the letter O"></span>
          <span>WARD</span>
        </span>
        <span class="title__line--mid">A BRIGHTER</span>
        <span class="title__line--end">MORNING</span>
      </h1>
      <footer class="author-band">
        <span class="author-band__name">DORIAN WAITE</span>
      </footer>
    </article>
  </main>
</body>
</html>
```